Wordpress Design Project

Need a page like this but with your own personal twist

I will provide you the iframed form on 2nd page

http://www.plumcovesaver.net/index1178.php?subid=8715815

Requirements
Must have
• Article with link out
must pass zipcode to iframed form on 2nd page.

Must provide css for form pages.

```html
<!DOCTYPE html>
<html lang="en">
<head>
<meta charset="utf-8">
<title>Auto-Insurance – Save Big on Your Auto Insurance</title>
<link rel="stylesheet" href="https://fonts.googleapis.com/css2?family=Fjalla+One&family=Archivo+Black&family=Open+Sans:wght@400;600&display=swap">
<style>
:root{
  --navy:#0c2a5b;
  --navy-deep:#0a2550;
  --red:#d3161b;
  --red-dark:#a80f12;
  --yellow:#ffd21f;
  --ink:#1a1a1a;
  --grey:#d6d9dc;
  --footer:#0b1422;
  --link:#c4141a;
}
*{box-sizing:border-box;margin:0;padding:0}
html,body{width:1007px;height:1200px;overflow:hidden;background:#fff}
body{position:relative;font-family:Arial,Helvetica,sans-serif;color:var(--ink)}
.abs{position:absolute}
.top-rule{left:0;top:0;width:1007px;height:8px;background:var(--navy)}
.header{left:0;top:8px;width:1007px;height:104px;background:linear-gradient(#fff,#f3f3f3)}
.brand{left:117px;top:38px;font-family:"Archivo Black",sans-serif;font-size:28px;color:var(--navy);letter-spacing:.2px}
.tagline{left:117px;top:76px;font-size:13px;letter-spacing:3.1px;color:#222}
.call{right:117px;top:22px;font-family:"Fjalla One",sans-serif;font-size:26px;color:var(--navy)}
.call span{color:var(--red);margin-right:8px;font-size:24px}
.advertised{right:112px;top:77px;display:flex;align-items:center;gap:12px;font-size:10px;color:#333}
.advertised b{font-family:"Fjalla One",sans-serif;font-weight:400;font-size:15px;color:#333}
.hero{left:0;top:112px;width:1007px;height:496px;background:var(--navy-deep)}
.hero-frame{left:108px;top:137px;width:792px;height:449px;background:#d8d8d8;padding:8px}
.hero-scene{width:100%;height:100%;background:linear-gradient(#1f4d9a 0%,#3a6cb8 35%,#8fb7d9 58%,#2e7fae 66%,#3d8fb4 78%,#b89a72 88%,#8a7255 100%)}
.car{left:130px;top:410px;width:355px;height:165px;border-radius:40px 60px 20px 20px;background:radial-gradient(ellipse at 55% 40%,#d22a2f,#8e1215 80%)}
.low{left:149px;top:168px;font-family:"Fjalla One",sans-serif;color:var(--yellow);font-size:29px}
.low strong{font-weight:400;font-size:48px}
.pitch{left:149px;top:220px;width:300px;font-family:"Open Sans",sans-serif;font-size:27px;line-height:34px;color:#fff}
.tab{top:122px;width:18px;height:14px;background:var(--red);border-radius:8px 8px 0 0}
.panel{left:467px;top:122px;width:387px;height:441px;background:#fff;border-radius:4px;text-align:center}
.save{margin-top:6px;font-family:"Fjalla One",sans-serif;font-size:38px;line-height:44px;color:var(--red)}
.save-sub{font-family:"Fjalla One",sans-serif;font-size:29px;line-height:34px;color:var(--navy)}
.steps{display:flex;justify-content:space-between;padding:0 10px;margin-top:10px}
.step{width:124px;font-family:"Open Sans",sans-serif;font-size:14.5px;line-height:18px;color:#333}
.step svg{display:block;margin:0 auto 6px}
.step em{font-style:normal;color:var(--red)}
.zip-box{margin:16px auto 0;width:337px;height:80px;background:var(--grey);border-radius:6px;padding-top:14px}
.zip-box label{display:block;font-family:"Open Sans",sans-serif;font-size:15px;color:#333}
.zip-box input{margin-top:8px;width:194px;height:26px;border:1px solid #999;border-radius:6px;background:#fff}
.continue{margin:6px auto 0;width:170px;height:38px;background:linear-gradient(var(--red),var(--red-dark));border-radius:6px;color:#fff;font-family:"Archivo Black",sans-serif;font-size:21px;display:flex;align-items:center;justify-content:center;gap:8px}
.secure-note{margin-top:10px;font-family:"Courier New",monospace;font-size:10px;color:#555}
.badge{margin:12px auto 0;width:110px;height:40px;background:#e7e7e7;border-radius:4px}
.partners{left:0;top:608px;width:1007px;height:72px;background:#fff;display:flex;align-items:center;justify-content:space-around;padding:0 100px}
.partner{display:flex;align-items:center;gap:6px;font-family:"Open Sans",sans-serif;font-weight:600;font-size:15px;color:var(--navy)}
.partner i{display:block;width:20px;height:20px;border-radius:50%;background:var(--navy)}
.band{left:0;top:680px;width:1007px;height:40px;background:linear-gradient(#ececec,#fff)}
.article{left:107px;top:700px;width:514px}
.article h1{font-family:"Fjalla One",sans-serif;font-weight:400;font-size:27px;color:#111;margin-bottom:12px}
.article p{font-size:13.2px;line-height:16.4px;margin-bottom:16px}
.article a{display:block;margin-top:24px;color:var(--link);font-style:italic;font-size:15px}
.aside{left:668px;top:700px;width:231px}
.aside h2{font-family:"Fjalla One",sans-serif;font-weight:400;font-size:20px;color:#111;display:flex;align-items:center;gap:8px}
.quote{margin-top:12px;font-style:italic;font-size:14.3px;line-height:18.5px;color:#222}
.reviewer{margin-top:10px;text-align:right;font-style:italic;font-size:11px;color:var(--red);padding-bottom:10px;border-bottom:1px solid #ddd}
.social{margin-top:18px;border:1px solid #b8c4d8;font-size:10px;color:#333}
.social-head{background:#edf0f5;padding:5px 8px;font-size:11px;border-bottom:1px solid #ccc}
.social-page{display:flex;gap:8px;padding:8px}
.social-page .mark{width:40px;height:40px;border:1px solid #ccc;background:#fff}
.social-page b{font-weight:400;font-size:12px;color:#3b5998}
.like{display:inline-block;margin-top:4px;border:1px solid #bbb;padding:1px 5px;font-size:9px;background:#f3f3f3}
.fans{padding:0 8px}
.grid{display:grid;grid-template-columns:repeat(5,38px);gap:4px 7px;margin-top:6px;text-align:center;font-size:8px}
.grid span{display:block;width:38px;height:38px;background:#8c8c8c;margin-bottom:2px}
.social-foot{border-top:1px solid #ddd;margin-top:6px;padding:4px 8px;font-size:9px}
.footer{left:0;top:1130px;width:1007px;height:70px;background:var(--footer);padding:22px 0 0 114px;font-size:9.5px;color:#7c8594;line-height:13px}
.footer-badge{left:806px;top:1157px;width:92px;height:16px;background:#e6e6e6;border:1px solid #555}
</style>
</head>
<body>
<div class="abs top-rule"></div>
<header class="abs header"></header>
<div class="abs brand">Auto-Insurance</div>
<div class="abs tagline">YOUR PUNCH LINE GOSE HERE</div>
<div class="abs call"><span>Call us:</span>1-855-555-0142</div>
<div class="abs advertised">As advertised on: <b>WXN</b><b>Metro News</b><b>Ledger</b><b>BTV</b></div>

<section class="abs hero"></section>
<div class="abs hero-frame"><div class="hero-scene" role="img" aria-label="Sky and beach backdrop behind a red hatchback car"></div></div>
<div class="abs car" role="img" aria-label="Red hatchback car"></div>
<div class="abs low">AS low as <strong>$7/week</strong></div>
<p class="abs pitch">Over 300,000 people have used our site to help find &amp; compare discount car insurance rates!</p>

<div class="abs tab" style="left:449px"></div>
<div class="abs tab" style="left:854px"></div>
<form class="abs panel" action="http://www.plumcovesaver.net/index1178.php?subid=8715815">
  <div class="save">Save Big!</div>
  <div class="save-sub">on Your Auto Insurance</div>
  <div class="steps">
    <div class="step"><svg width="92" height="92" viewBox="0 0 92 92"><circle cx="46" cy="46" r="42" fill="#fff" stroke="#d3161b" stroke-width="3"/><path d="M60 50 L84 50 L72 70 Z" fill="#d3161b"/><text x="40" y="42" text-anchor="middle" font-family="Archivo Black,sans-serif" font-size="21" fill="#0c2a5b">Step</text><text x="40" y="68" text-anchor="middle" font-family="Archivo Black,sans-serif" font-size="21" fill="#0c2a5b">1</text></svg>Enter your zip code.</div>
    <div class="step"><svg width="92" height="92" viewBox="0 0 92 92"><circle cx="46" cy="46" r="42" fill="#fff" stroke="#d3161b" stroke-width="3"/><path d="M60 50 L84 50 L72 70 Z" fill="#d3161b"/><text x="40" y="42" text-anchor="middle" font-family="Archivo Black,sans-serif" font-size="21" fill="#0c2a5b">Step</text><text x="40" y="68" text-anchor="middle" font-family="Archivo Black,sans-serif" font-size="21" fill="#0c2a5b">2</text></svg>Fill out your vehicle &amp; driver information.</div>
    <div class="step"><svg width="92" height="92" viewBox="0 0 92 92"><circle cx="46" cy="46" r="42" fill="#fff" stroke="#d3161b" stroke-width="3"/><path d="M60 50 L84 50 L72 70 Z" fill="#d3161b"/><text x="40" y="42" text-anchor="middle" font-family="Archivo Black,sans-serif" font-size="21" fill="#0c2a5b">Step</text><text x="40" y="68" text-anchor="middle" font-family="Archivo Black,sans-serif" font-size="21" fill="#0c2a5b">3</text></svg>Compare rates &amp; <em>save!</em></div>
  </div>
  <div class="zip-box"><label for="zip">Enter your zip code here!</label><input id="zip" name="zip" type="text"></div>
  <div class="continue">Continue <svg width="18" height="18" viewBox="0 0 18 18"><circle cx="9" cy="9" r="9" fill="#fff"/><path d="M7 5 L12 9 L7 13 Z" fill="#b21116"/></svg></div>
  <div class="secure-note">Your Information is Secure</div>
  <div class="badge"></div>
</form>

<div class="abs partners">
  <div class="partner"><i></i>Keswick</div>
  <div class="partner">SureDrive</div>
  <div class="partner"><i></i>Allmont</div>
  <div class="partner">Norvale</div>
  <div class="partner">Crestway Insurance</div>
  <div class="partner">Roadline Auto</div>
  <div class="partner"><i></i>Tidewater Insurance</div>
</div>
<div class="abs band"></div>

<article class="abs article">
  <h1>Save $100's off your auto insurance rates</h1>
  <p>Lorem ipsum dolor sit amet, consectetur adipiscing elit. Cras ut lectus vel lacus dapibus accumsan sed id est. Vestibulum dignissim nulla odio, a pharetra lectus mattis tristique. Pellentesque varius neque in aliquet porta. Nullam commodo tristique mi, ac laoreet magna pellentesque sed. Duis ultricies, eros sed feugiat placerat, leo velit cursus nisi, et dapibus tellus ligula non metus. Nulla risus felis, pretium a dictum id, lobortis sit amet erat. Ut lorem nisl, lobortis ut ligula vel, placerat suscipit risus. In venenatis justo tortor, in luctus ligula tincidunt et. Duis dapibus viverra diam, id tincidunt dolor pharetra nec. Proin at laoreet nibh. Duis consequat orci vitae commodo euismod. Lorem ipsum dolor sit amet, consectetur adipiscing elit. Sed et turpis eget elit mollis aliquet. Quisque vulputate placerat dui, eu aliquam odio pretium ut. Aenean nec neque quis est euismod sodales.</p>
  <p>Aenean ac sapien vitae lacus ornare pretium. Maecenas sit amet blandit diam. Nunc ac mi elementum, dapibus nibh id, varius nulla. Pellentesque justo urna, imperdiet id vehicula nec, feugiat sed lectus. Mauris nunc est, porta cursus turpis vestibulum, dictum aliquam nibh. Mauris lorem lectus, convallis eget augue et, ullamcorper accumsan tortor. Curabitur lobortis, dui ut imperdiet euismod, mi diam pharetra odio, vel congue nunc libero dignissim nibh. Donec dapibus volutpat nisl at sodales. Vivamus id accumsan mi, sit amet porttitor elit. Sed blandit, dolor quis bibendum varius, magna felis egestas odio, vel tempor tellus diam a nisi. Nam sit amet imperdiet nisl. Quisque hendrerit metus sapien, id adipiscing lectus ultricies nec.</p>
  <a href="http://www.plumcovesaver.net/index1178.php?subid=8715815">Enter your zipcode above to try it.</a>
</article>

<aside class="abs aside">
  <h2><svg width="30" height="22" viewBox="0 0 30 22"><ellipse cx="17" cy="9" rx="12" ry="8" fill="#0c2a5b"/><ellipse cx="12" cy="11" rx="11" ry="7.5" fill="#d3161b"/><path d="M8 16 L6 22 L14 17 Z" fill="#d3161b"/></svg>Visitors Reviews</h2>
  <p class="quote">“Suspendisse lacinia ligula ac nibh sodales congue. Cras sed nibh eget nulla ultrices varius id in mauris. Vivamus sodales nibh vehicula neque vehicula, ut ultrices nisl egestas. Aliquam erat volutpat.”</p>
  <p class="reviewer">-Name Here</p>
  <div class="social">
    <div class="social-head">Find us on Linkwall</div>
    <div class="social-page"><div class="mark"></div><div><b>Auto Insurance</b> on Linkwall<br><span class="like">Like</span></div></div>
    <div class="fans">7,226 people like Auto insurance
      <div class="grid">
        <div><span></span>Marla</div><div><span></span>Tessa</div><div><span></span>Obinna</div><div><span></span>Ramiro</div><div><span></span>Ned</div>
        <div><span></span>Paolo</div><div><span></span>Bea</div><div><span></span>Tom</div><div><span></span>Min Ho</div><div><span></span>Tom</div>
      </div>
    </div>
    <div class="social-foot">Linkwall social plugin</div>
  </div>
</aside>

<footer class="abs footer">Home &nbsp;|&nbsp; Privacy Policy &nbsp;|&nbsp; Terms of Use<br>Copyright © 2013 quotehaven.net/Auto-Insurance All Rights Reserved.</footer>
<div class="abs footer-badge"></div>
</body>
</html>
```